Wexbridge Home Services Web Site

Design Web site with 3-4 pages: Home, About Us, Services and Order form / Schedule Appointment (which will likely be link to Tallyo App and Ledgerpine integration.)
Services include: Dryer Vent Cleaning, AC Cleaning, Difficult-to-Reach Light Bulb replacement, Wood Repair and Home Maintenance Plans including Fire Safety Checks and Filter Replacement.

Target Market(s)

Luxury Home Owners, Professionals (Dr's/lawyers) and Seniors

Industry/Entity Type

Home Maintenance

Coding

Coded - Design and coding required

Requirements
Must have
• Tagline - Where Home Maintenance is Effortless

```html
<!DOCTYPE html>
<html lang="en">
<head>
<meta charset="utf-8">
<title>Wexbridge Home Services</title>
<link href="https://fonts.googleapis.com/css2?family=Outfit:wght@400;500;600&display=swap" rel="stylesheet">
<style>
:root{
  --gold:#e2a82a;
  --gold-deep:#d39a1d;
  --gold-soft:#f0c35a;
  --ink:#3f3f41;
  --text:#2b2b2b;
  --band:#4b4b4d;
  --white:#ffffff;
}
*{box-sizing:border-box;margin:0;padding:0}
html,body{width:1200px;height:3331px;overflow:hidden}
body{position:relative;font-family:'Outfit',sans-serif;color:var(--text);background:var(--white)}
.abs{position:absolute}
.brand{display:flex;align-items:center;gap:10px;font-weight:600;color:var(--gold);font-size:19px;line-height:1.15;letter-spacing:.5px}
.brand .dot{width:34px;height:34px;border-radius:50%;background:var(--gold);flex:none}
.nav{display:flex;gap:37px;font-size:16px;color:var(--text)}
.nav .active{color:var(--gold);border-bottom:2px solid var(--gold);padding-bottom:4px}
.btn{display:inline-flex;align-items:center;justify-content:center;gap:10px;font-size:15px;font-weight:500;border-radius:3px}
.btn-gold{background:var(--gold);color:#fff;box-shadow:0 4px 10px rgba(226,168,42,.35)}
.btn-outline{border:1.5px solid var(--gold);color:var(--ink);background:#fff}
.btn-white{background:#fff;color:var(--ink);box-shadow:0 3px 8px rgba(0,0,0,.12)}
.tagline{font-size:15px;font-weight:500;letter-spacing:1.5px;text-transform:uppercase;color:var(--gold)}
.h2{font-size:44px;font-weight:500;line-height:1.08;color:var(--ink)}
.h2 span{color:var(--gold);display:block}
.lede{font-size:15.5px;line-height:26px;color:var(--text)}
.photo{border-radius:6px}
.partners{display:flex;justify-content:space-between;align-items:center;color:#fff;font-size:21px;font-weight:500}
.partners div{display:flex;align-items:center;gap:8px}
.partners i{width:22px;height:22px;border-radius:50%;background:#cfcfcf;display:block}
.svc h3{font-size:27px;font-weight:500;line-height:32px;color:var(--ink);margin-bottom:18px}
.svc p{font-size:15.5px;line-height:26px}
.card-active{background:#fff;box-shadow:0 6px 30px rgba(0,0,0,.08);border-radius:6px}
.about-text{color:#fff}
.about-text .h2{color:#fff}
.about-text .h2 span{color:var(--ink)}
.about-text p{font-size:15.5px;line-height:26px;margin-bottom:20px}
.review{background:#fff;box-shadow:0 6px 30px rgba(0,0,0,.07);border-radius:6px;padding:38px 28px}
.review .top{display:flex;align-items:center;gap:24px}
.quote{font-size:96px;font-weight:600;line-height:60px;height:56px;color:var(--ink);font-family:Georgia,serif}
.stars{color:var(--gold);font-size:28px;letter-spacing:3px}
.who{display:flex;align-items:center;gap:18px;margin:26px 0 30px}
.avatar{width:70px;height:70px;border-radius:50%;background:linear-gradient(135deg,#5b4a3f,#2e2a28);flex:none}
.who b{font-size:21px;font-weight:500;color:var(--ink);white-space:nowrap}
.review p{font-size:15.5px;line-height:26px}
.footer{background:var(--gold);color:#fff}
.footnav{display:flex;gap:35px;font-size:18px;font-weight:500;justify-content:center}
.social{display:flex;gap:14px;justify-content:center}
.social i{width:22px;height:22px;border-radius:50%;background:#fff;display:block}
</style>
</head>
<body>

<!-- Hero -->
<svg class="abs" style="left:0;top:0" width="1200" height="612" aria-hidden="true">
  <polygon points="850,0 1200,0 1200,612 630,612" fill="var(--gold)"/>
  <circle cx="730" cy="385" r="123" fill="#cfcfcf"/>
</svg>
<div class="abs" role="img" aria-label="Two smiling cleaning technicians in grey aprons with arms crossed" style="left:650px;top:136px;width:527px;height:476px;background:linear-gradient(180deg,#4a4a4a 0%,#5e5e5e 55%,#707070 100%);border-radius:200px 200px 0 0;opacity:.9"></div>
<div class="abs" role="img" aria-label="Orange upright vacuum cleaner" style="left:0;top:427px;width:187px;height:185px;background:linear-gradient(135deg,#f08a2a,#c9641a 60%,#7a7a7a);border-radius:0 60px 0 0"></div>

<header>
  <div class="abs brand" style="left:111px;top:40px"><span class="dot"></span><span>Wexbridge<br>Home Services</span></div>
  <nav class="abs nav" style="left:302px;top:79px">
    <span class="active">Home</span><span>Service</span><span>About Us</span><span>Testimonials</span><span>Contact</span>
  </nav>
  <svg class="abs" style="left:861px;top:82px" width="16" height="16" viewBox="0 0 16 16" aria-hidden="true"><circle cx="6.5" cy="6.5" r="4.5" fill="none" stroke="#fff" stroke-width="2"/><path d="M10 10l4 4" stroke="#fff" stroke-width="2"/></svg>
  <div class="abs btn btn-white" style="left:921px;top:67px;width:168px;height:44px">Get in Touch
    <svg width="16" height="16" viewBox="0 0 24 24" aria-hidden="true"><path d="M6.6 10.8a15 15 0 006.6 6.6l2.2-2.2c.3-.3.7-.4 1-.2 1.1.4 2.3.6 3.6.6.6 0 1 .4 1 1V20c0 .6-.4 1-1 1A17 17 0 013 4c0-.6.4-1 1-1h3.5c.6 0 1 .4 1 1 0 1.3.2 2.5.6 3.6.1.3 0 .7-.2 1z" fill="none" stroke="var(--gold)" stroke-width="2"/></svg>
  </div>
</header>

<section>
  <div class="abs tagline" style="left:111px;top:180px">Where Home Maintenance is Effortless</div>
  <h1 class="abs" style="left:111px;top:218px;font-size:50px;font-weight:500;line-height:52px;color:var(--ink)">Keeping Your Home<br><span style="color:var(--gold)">Clean &amp; Comfortable</span></h1>
  <svg class="abs" style="left:583px;top:213px" width="80" height="60" aria-hidden="true">
    <g stroke="var(--gold)" stroke-width="2.5" stroke-linecap="round"><circle cx="26" cy="33" r="5" fill="var(--gold)"/><path d="M26 17v6M26 43v6M10 33h6M36 33h6M15 22l4 4M33 40l4 4M15 44l4-4M33 26l4-4"/></g>
    <g stroke="var(--gold)" stroke-width="1.5"><circle cx="66" cy="10" r="2.5" fill="var(--gold)"/><path d="M66 1v4M66 15v4M57 10h4M71 10h4"/></g>
  </svg>
  <p class="abs lede" style="left:111px;top:343px;width:440px">Expert maintenance services tailored to protect<br>your home and give you peace of mind.<br>Schedule your appointment with <span style="color:var(--gold)">Wexbridge Homes</span> today.</p>
  <div class="abs btn btn-gold" style="left:111px;top:452px;width:258px;height:43px">Schedule an Appointment
    <svg width="16" height="16" viewBox="0 0 24 24" aria-hidden="true"><path d="M6.6 10.8a15 15 0 006.6 6.6l2.2-2.2c.3-.3.7-.4 1-.2 1.1.4 2.3.6 3.6.6.6 0 1 .4 1 1V20c0 .6-.4 1-1 1A17 17 0 013 4c0-.6.4-1 1-1h3.5c.6 0 1 .4 1 1 0 1.3.2 2.5.6 3.6.1.3 0 .7-.2 1z" fill="none" stroke="#fff" stroke-width="2"/></svg>
  </div>
  <svg class="abs" style="left:384px;top:451px" width="46" height="46" aria-hidden="true"><circle cx="23" cy="23" r="22" fill="#fff" style="filter:drop-shadow(0 2px 4px rgba(0,0,0,.15))"/><polygon points="18,15 31,23 18,31" fill="var(--gold)"/></svg>
  <div class="abs" style="left:445px;top:463px;font-size:16px;font-weight:500;color:var(--ink)">See How We Work</div>
</section>

<!-- Partner band -->
<div class="abs" style="left:0;top:612px;width:1200px;height:102px;background:var(--band)"></div>
<div class="abs partners" style="left:111px;top:648px;width:978px">
  <div><i></i>Northvale</div><div><i></i>Corvine</div><div><i></i>Peakline</div><div><i></i>Oriel</div><div><i></i>Summa</div>
</div>

<!-- Services -->
<h2 class="abs h2" style="left:111px;top:793px">Services &amp; Plans<span>We Offer You</span></h2>
<p class="abs lede" style="left:514px;top:808px;width:575px">From dryer vent cleaning to wood repair and customized maintenance plans, we handle the hard-to-do tasks so you don't have to. Trust us to protect your home with expert care and reliable service.</p>

<div class="abs card-active" style="left:59px;top:950px;width:404px;height:440px"></div>
<svg class="abs" style="left:111px;top:992px" width="76" height="81" viewBox="0 0 76 81" aria-hidden="true" fill="none" stroke="var(--gold)" stroke-width="2.5">
  <rect x="4" y="2" width="50" height="64" rx="3"/><path d="M4 14h50"/><circle cx="29" cy="40" r="16"/><circle cx="29" cy="40" r="10"/><path d="M54 46c10 0 14 6 14 12s-4 10-10 10H4"/><path d="M4 74h60"/>
</svg>
<svg class="abs" style="left:513px;top:992px" width="84" height="81" viewBox="0 0 84 81" aria-hidden="true" fill="none" stroke="var(--gold)" stroke-width="2.5">
  <rect x="2" y="16" width="78" height="36" rx="4"/><path d="M2 40h78M10 46h62"/><circle cx="14" cy="28" r="4"/><circle cx="26" cy="28" r="4"/><path d="M50 2l20 20M56 20l-12 10"/><path d="M24 60c-3 6 3 8 0 14M36 60c-3 6 3 8 0 14M48 60c-3 6 3 8 0 14"/>
</svg>
<svg class="abs" style="left:854px;top:992px" width="92" height="81" viewBox="0 0 92 81" aria-hidden="true" fill="none" stroke="var(--gold)" stroke-width="2.5">
  <path d="M14 2l14 10-6 8-14-10z"/><path d="M22 18l58 52-6 8L16 28"/><path d="M2 46h40M2 58h60M2 70h88M2 78h88M2 46v32"/>
</svg>

<div class="abs svc" style="left:111px;top:1090px;width:300px">
  <h3>Dryer Vent<br>Cleaning</h3>
  <p>Keep your dryer safe and efficient by<br>removing lint &amp; blockages also reducing<br>fire risks and improve performance with<br>our expert cleaning service.</p>
</div>
<div class="abs btn btn-gold" style="left:104px;top:1292px;width:308px;height:41px;justify-content:space-between;padding:0 28px">Learn More About Service
  <svg width="22" height="22" aria-hidden="true"><circle cx="11" cy="11" r="10" fill="#fff"/><path d="M7 11h8M12 7l4 4-4 4" stroke="var(--gold)" stroke-width="2" fill="none"/></svg>
</div>

<div class="abs svc" style="left:513px;top:1090px;width:300px">
  <h3>Air Conditioner<br>Cleaning</h3>
  <p>Enhance your indoor air quality and air<br>conditioning operation with professional<br>cleaning that removes dust, mold, and<br>debris from your system.</p>
</div>
<div class="abs btn btn-outline" style="left:513px;top:1292px;width:131px;height:41px">Learn More</div>

<div class="abs svc" style="left:856px;top:1090px;width:310px">
  <h3>Wooden Furniture<br>Repairs</h3>
  <p>Restore your wood surfaces from<br>scratches, cracks, or damage with repair<br>services that match finishes and also<br>reinforce strength.</p>
</div>
<div class="abs btn btn-outline" style="left:856px;top:1292px;width:131px;height:41px">Learn More</div>

<svg class="abs" style="left:500px;top:1405px" width="200" height="70" aria-hidden="true">
  <rect x="1" y="15" width="198" height="42" fill="#fff" stroke="var(--gold)" stroke-width="1.5"/>
  <circle cx="138" cy="36" r="33" fill="#f0f0f0"/>
  <path d="M76 36H46M56 27l-10 9 10 9" stroke="#bbb" stroke-width="3" fill="none"/>
  <path d="M124 36h28M142 27l10 9-10 9" stroke="var(--gold)" stroke-width="3" fill="none"/>
</svg>

<!-- About -->
<div class="abs" role="img" aria-label="Warm golden wood floor texture" style="left:0;top:1563px;width:1200px;height:631px;background:linear-gradient(135deg,var(--gold-deep) 0%,var(--gold) 45%,var(--gold-soft) 100%)"></div>
<div class="abs" role="img" aria-label="Vacuum cleaner" style="left:960px;top:2040px;width:240px;height:154px;background:linear-gradient(135deg,rgba(90,70,20,.15),rgba(60,50,20,.45));border-radius:120px 0 0 0"></div>
<div class="abs" style="left:123px;top:1663px;width:411px;height:439px;background:var(--band);border-radius:6px"></div>
<div class="abs photo" role="img" aria-label="Cleaner in red overalls mopping a bright dining room floor" style="left:114px;top:1680px;width:403px;height:439px;background:linear-gradient(160deg,#e9e9e7 0%,#cfd2d3 55%,#b9bcbd 100%)"></div>
<div class="abs about-text" style="left:623px;top:1680px;width:470px">
  <h2 class="h2">About<span>Wexbridge Homes</span></h2>
  <p style="margin-top:26px">At Wexbridge Homes, we believe a well-maintained home is a happy<br>home. With years of experience serving our community,<br>we specialize in detailed home maintenance services that help<br>you save time, reduce risks, and protect your investment.</p>
  <p>Our mission is to provide exceptional, trustworthy service with a<br>personal touch. We stay up-to-date with the latest industry<br>practices and use quality products to ensure lasting results.</p>
</div>
<div class="abs btn" style="left:623px;top:2031px;width:167px;height:42px;background:#fff;color:var(--ink)">Learn More
  <svg width="17" height="17" aria-hidden="true"><circle cx="8.5" cy="8.5" r="7.5" fill="none" stroke="var(--gold)" stroke-width="1.5"/><path d="M8.5 7.5v5M8.5 4.5v1.2" stroke="var(--gold)" stroke-width="1.5"/></svg>
</div>

<!-- Testimonials -->
<h2 class="abs h2" style="left:111px;top:2302px">Hear What<span>People Talk of Us</span></h2>
<p class="abs lede" style="left:514px;top:2317px;width:575px">From dryer vent cleaning to wood repair and customized maintenance plans, we handle the hard-to-do tasks so you don't have to. Trust us to protect your home with expert care and reliable service.</p>

<div class="abs" style="left:114px;top:2463px;width:1200px;display:flex;gap:18px">
  <div class="review" style="width:293px;height:410px;flex:none">
    <div class="top"><div class="quote">&#8220;</div><div class="stars">★★★★★</div></div>
    <div class="who"><div class="avatar" role="img" aria-label="Customer portrait"></div><b>Daniel Hart M.</b></div>
    <p>"I'm so impressed with Wexbridge Homes! Their dryer vent cleaning made my laundry room safer and more efficient. The team was professional, friendly and is very much highly recommend!"</p>
  </div>
  <div class="review" style="width:294px;height:410px;flex:none">
    <div class="top"><div class="quote">&#8220;</div><div class="stars">★★★★★</div></div>
    <div class="who"><div class="avatar" role="img" aria-label="Customer portrait"></div><b>Elena Brooks S.</b></div>
    <p>"I'm so impressed with Wexbridge Homes! Their dryer vent cleaning made my laundry room safer and more efficient. The team was professional, friendly and is very much highly recommend!"</p>
  </div>
  <div class="review" style="width:294px;height:410px;flex:none">
    <div class="top"><div class="quote">&#8220;</div><div class="stars">★★★★★</div></div>
    <div class="who"><div class="avatar" role="img" aria-label="Customer portrait"></div><b>Simon Pryce R.</b></div>
    <p>"I'm so impressed with Wexbridge Homes! Their dryer vent cleaning made my laundry room safer and more efficient. The team was professional, friendly and is very much highly recommend!"</p>
  </div>
  <div class="review" style="width:294px;height:410px;flex:none">
    <div class="top"><div class="quote">&#8220;</div><div class="stars">★★★★★</div></div>
    <div class="who"><div class="avatar" role="img" aria-label="Customer portrait"></div><b>Dana Wells</b></div>
    <p>"I'm so impressed with Wexbridge Homes! Their dryer vent cleaning made my laundry room safer and more efficient. The team was professional, friendly and is very much highly recommend!"</p>
  </div>
</div>

<!-- Footer -->
<footer class="abs footer" style="left:0;top:2979px;width:1200px;height:352px">
  <div class="abs brand" style="left:0;top:52px;width:1200px;justify-content:center;color:var(--ink);font-size:26px;text-align:center">
    <span class="dot" style="background:var(--ink);width:44px;height:44px"></span><span>Wexbridge<br>Home Services</span>
  </div>
  <nav class="abs footnav" style="left:0;top:189px;width:1200px">
    <span>Home</span><span>Products</span><span>About</span><span>Categories</span><span>Testimonials</span><span>Contact</span>
  </nav>
  <div class="abs social" style="left:0;top:246px;width:1200px"><i></i><i></i><i></i><i></i></div>
  <div class="abs" style="left:0;top:300px;width:1200px;text-align:center;font-size:12px">© 2025 Wexbridge Home Services. All Rights Reserved.</div>
</footer>

</body>
</html>
```